Business Card Design Project

We have a logo, but would like to expand the use of it into a business card design. We are a B2B technology exchange platform for institutional investors to invest excess cash into short term assets matching their credit and pricing parameters. The assets are fractionalized and investors invest in portions.

Our customers are large, institutional, financial companies who are a bit traditional. We are high energy rebels with a cause...we are a disruptive technology and want to be viewed as a game changer but we need to present an image of trustworthiness and secure.

We are open not only to the image design but the material, die cut, etc. but want to stay in the traditional size of a business card.

We have other formats of the logo if needed. Our website is www.brambleharbor.com

I have posted a powerpoint template that we have been using.  This should not be considered the template we will use (after business cards we will have another project to incorporate business card design into powerpoint template) but just to give you a flavor of where we have been and have used in the past.

Target Market(s)

Institutional investors, asset managers, large fund institutions

Industry/Entity Type

Financial

Requirements
Must have
• Our logo
Traditional size
Nice to have
• unique use of logo, unique material, die cut, etc
Crisp, clean look
Use of both sides of card in a creative manner

```html
<!DOCTYPE html>
<html lang="en">
<head>
<meta charset="utf-8">
<title>Bramble Harbor Business Card</title>
<link rel="stylesheet" href="https://fonts.googleapis.com/css2?family=Exo+2:wght@400;600;700&display=swap">
<style>
  :root {
    --backdrop: #e4e4e2;
    --card: #ffffff;
    --accent: #f0901e;
    --ink: #4a4a4a;
    --muted: #8a8a8a;
    --brand: #6d6d6d;
    --watermark: #efefef;
  }
  * { box-sizing: border-box; margin: 0; padding: 0; }
  html, body {
    width: 1200px; height: 871px; overflow: hidden;
    background: var(--backdrop);
    font-family: "Exo 2", sans-serif;
  }
  .stage {
    width: 1200px; height: 871px;
    display: flex; flex-direction: column;
    align-items: center; justify-content: center; gap: 34px;
  }
  .card {
    position: relative;
    width: 660px; height: 377px;
    background: var(--card);
    overflow: hidden;
    box-shadow: 0 6px 20px rgba(0,0,0,0.12);
  }
  .card-watermark { position: absolute; }
  .card--back .card-watermark { right: -60px; top: -150px; width: 400px; height: 400px; }
  .card--front .card-watermark { right: -70px; top: 110px; width: 360px; height: 360px; }

  .brand { position: absolute; display: flex; align-items: center; }
  .brand-dot { border-radius: 50%; background: var(--accent); flex: none; }
  .brand-name {
    font-weight: 700; color: var(--brand);
    text-transform: uppercase; letter-spacing: 1px; white-space: nowrap;
  }
  .card--back .brand { left: 52px; top: 160px; gap: 14px; }
  .card--back .brand-dot { width: 26px; height: 26px; }
  .card--back .brand-name { font-size: 40px; }
  .card--front .brand { left: 40px; top: 34px; gap: 9px; }
  .card--front .brand-dot { width: 14px; height: 14px; }
  .card--front .brand-name { font-size: 23px; }

  .person { position: absolute; left: 40px; top: 104px; }
  .person-name { font-weight: 700; font-size: 21px; color: var(--accent); line-height: 1.2; }
  .person-title { font-size: 14px; color: var(--muted); }
  .address {
    position: absolute; left: 40px; top: 186px;
    font-size: 16px; line-height: 1.5; color: var(--ink); font-style: normal;
  }
  .contact {
    position: absolute; right: 38px; bottom: 30px;
    text-align: right; font-size: 16.5px; line-height: 1.5;
    color: var(--ink); letter-spacing: 0.4px; white-space: nowrap;
  }
  .contact-label { color: var(--accent); font-weight: 700; margin-right: 4px; }
  .contact-row span + span { margin-left: 20px; }
</style>
</head>
<body>
<main class="stage">
  <section class="card card--back" aria-label="Bramble Harbor business card, back">
    <svg class="card-watermark" viewBox="0 0 400 400" aria-hidden="true">
      <circle cx="200" cy="200" r="200" fill="var(--watermark)"/>
    </svg>
    <div class="brand">
      <span class="brand-dot" aria-hidden="true"></span>
      <span class="brand-name">Bramble Harbor</span>
    </div>
  </section>

  <section class="card card--front" aria-label="Bramble Harbor business card, front">
    <svg class="card-watermark" viewBox="0 0 360 360" aria-hidden="true">
      <circle cx="180" cy="180" r="180" fill="var(--watermark)"/>
    </svg>
    <header class="brand">
      <span class="brand-dot" aria-hidden="true"></span>
      <span class="brand-name">Bramble Harbor</span>
    </header>
    <div class="person">
      <p class="person-name">Tobias Renwick</p>
      <p class="person-title">Marketing Director</p>
    </div>
    <address class="address">
      2150 Harbor Crest Drive<br>
      Suite 410<br>
      Fairhaven, CA 90210
    </address>
    <div class="contact">
      <p class="contact-row">
        <span><span class="contact-label">W:</span>www.brambleharbor.com</span><span><span class="contact-label">P:</span>555.014.2290</span>
      </p>
      <p class="contact-row"><span class="contact-label">E:</span>Marketing@BrambleHarbor.com</p>
    </div>
  </section>
</main>
</body>
</html>
```